Pillow Company needs Pillow Insert Design

I just started a new pillow line with two pillow types. I have a hotel pillow and an organic pillow. I need two pillow insert signs designed that follow the same layout but are different color types. I want one sign to incorporate silver and white look and another sign to incorporate a green and white look (this one to look organic). They must have the same layout but different colors. I have include examples of what I want it to look like. In addition, I have uploaded the two hi res images for each sign. My logo is uploaded too.

I am open to other concepts and colors as long as it looks modern, clean and upscale. In addition, I need a Made in the USA logo on the pillow insert designs.

I have attached details on sign, images to be used, and examples that I like.

The Pillow Sign Size is 12 inches x 12 inches.

```html
<!DOCTYPE html>
<html lang="en">
<head>
<meta charset="utf-8">
<title>Lumarest Luxurious Pillow Insert</title>
<link rel="stylesheet" href="https://fonts.googleapis.com/css2?family=Arimo:wght@400;700&family=Didact+Gothic&display=swap">
<style>
  :root {
    --page-bg: #aeb5b7;
    --card-bg: #ffffff;
    --frame: #5d6466;
    --band: #c9cdcf;
    --band-line: #eef0f1;
    --ribbon: #aab1b3;
    --ink: #333638;
    --ink-soft: #3f4345;
    --bullet: #555a5c;
    --brand-green: #66cc33;
    --badge-blue: #1f3f97;
    --photo-light: #eef0f2;
    --photo-mid: #d9d4cf;
    --photo-warm: #c9a88c;
  }
  * { box-sizing: border-box; margin: 0; padding: 0; }
  html, body { width: 1200px; height: 1200px; overflow: hidden; }
  body { background: var(--page-bg); font-family: "Arimo", Arial, sans-serif; position: relative; }

  .insert { position: absolute; left: 150px; top: 173px; width: 902px; height: 903px; background: var(--card-bg); overflow: hidden; }
  .insert-frame { position: absolute; left: 10px; top: 23px; width: 880px; height: 866px; border: 4px solid var(--frame); z-index: 5; pointer-events: none; }

  .top-band { position: absolute; left: 20px; top: 35px; width: 856px; height: 232px; background: var(--band); }
  .brand-panel { position: absolute; left: 8px; top: 10px; width: 442px; height: 211px; border: 1px solid var(--band-line); }
  .brand { position: absolute; left: 80px; top: 8px; display: flex; align-items: center; gap: 14px; }
  .brand-mark { width: 76px; height: 66px; background: var(--brand-green); }
  .brand-name { font-size: 36px; font-weight: 700; color: var(--brand-green); letter-spacing: 0.5px; }
  .brand-rule { position: absolute; left: 10px; top: 86px; width: 421px; height: 1px; background: var(--band-line); }
  .product-title { position: absolute; left: 0; top: 93px; width: 100%; text-align: center; font-family: "Didact Gothic", Arial, sans-serif; font-weight: 400; font-size: 27px; letter-spacing: 4px; word-spacing: 14px; color: var(--ink); }
  .product-intro { position: absolute; left: 37px; top: 141px; font-size: 17px; line-height: 20px; color: var(--ink); word-spacing: 3.5px; }

  .feature-note { position: absolute; left: 462px; top: 55px; width: 394px; text-align: center; color: #ffffff; font-size: 16.5px; line-height: 20px; word-spacing: 2px; white-space: nowrap; }

  .feature-list { position: absolute; left: 30px; top: 287px; list-style: none; }
  .feature-list li { display: flex; align-items: center; height: 25px; font-size: 18.5px; color: var(--ink-soft); }
  .feature-list svg { width: 14px; height: 14px; margin-right: 19px; }

  .lifestyle-photo { position: absolute; left: 0; top: 524px; width: 902px; height: 379px;
    background: linear-gradient(160deg, var(--photo-light) 0%, var(--photo-mid) 45%, var(--photo-warm) 62%, var(--photo-light) 85%); }

  .ribbon { position: absolute; left: 392px; top: 458px; width: 510px; height: 125px; z-index: 3; }
  .ribbon-text { position: absolute; left: 434px; top: 503px; z-index: 4; color: #ffffff; font-size: 21px; line-height: 26px; letter-spacing: 0.3px; word-spacing: 3px; transform: rotate(-2.5deg); transform-origin: left top; white-space: nowrap; }

  .origin-badge { position: absolute; left: 747px; top: 810px; width: 129px; height: 70px; background: var(--badge-blue); border-radius: 3px; z-index: 4; }
</style>
</head>
<body>
  <div class="insert">
    <div class="top-band">
      <div class="brand-panel">
        <div class="brand">
          <span class="brand-mark"></span>
          <span class="brand-name">Lumarest</span>
        </div>
        <div class="brand-rule"></div>
        <h1 class="product-title">luxurious pillow</h1>
        <p class="product-intro">This pillow was designed to give you<br>the most comfortable night’s sleep in your life.<br>Designed for all types of sleep positions.</p>
      </div>
      <p class="feature-note">We added revolutionary features from<br>our advanced Super Soft Premium Memory<br>Foam that has an open cell structure design<br>thatrecovers quickly and does not trap heat to<br>our gel infused polyester fiber to<br>our 100% Certified Organic Cotton Fabric.</p>
    </div>

    <ul class="feature-list">
      <li><svg viewBox="0 0 16 16"><g fill="var(--bullet)"><rect x="7.2" y="1" width="1.6" height="14"/><rect x="1" y="7.2" width="14" height="1.6"/></g></svg>Made From the Finest Premium Materials</li>
      <li><svg viewBox="0 0 16 16"><g fill="var(--bullet)"><rect x="7.2" y="1" width="1.6" height="14"/><rect x="1" y="7.2" width="14" height="1.6"/></g></svg>Adjusts to your Body Weight and Temperature</li>
      <li><svg viewBox="0 0 16 16"><g fill="var(--bullet)"><rect x="7.2" y="1" width="1.6" height="14"/><rect x="1" y="7.2" width="14" height="1.6"/></g></svg>100% Certified Organic Cotton Fabric</li>
      <li><svg viewBox="0 0 16 16"><g fill="var(--bullet)"><rect x="7.2" y="1" width="1.6" height="14"/><rect x="1" y="7.2" width="14" height="1.6"/></g></svg>Cool Non-Allergenic, Anti-Microbial, and Hypoallergenic</li>
      <li><svg viewBox="0 0 16 16"><g fill="var(--bullet)"><rect x="7.2" y="1" width="1.6" height="14"/><rect x="1" y="7.2" width="14" height="1.6"/></g></svg>Conforms to Head and Neck for optimal Alignment during Sleep</li>
      <li><svg viewBox="0 0 16 16"><g fill="var(--bullet)"><rect x="7.2" y="1" width="1.6" height="14"/><rect x="1" y="7.2" width="14" height="1.6"/></g></svg>Mildew Proof and Dust Mite Resistant</li>
      <li><svg viewBox="0 0 16 16"><g fill="var(--bullet)"><rect x="7.2" y="1" width="1.6" height="14"/><rect x="1" y="7.2" width="14" height="1.6"/></g></svg>Quilvane Seal toxin free certified foam</li>
    </ul>

    <div class="lifestyle-photo" role="img" aria-label="Photo of a smiling family of three relaxing together on white pillows in bed"></div>

    <svg class="ribbon" viewBox="0 0 510 125" aria-hidden="true">
      <path d="M0,10 C150,28 330,0 510,6 L510,100 C360,92 200,130 0,112 Z" fill="var(--ribbon)"/>
    </svg>
    <p class="ribbon-text">Surround Yourself with the Best!<br>Individually Handcrafted and Made in USA</p>

    <div class="origin-badge" role="img" aria-label="Made in USA badge"></div>

    <div class="insert-frame"></div>
  </div>
</body>
</html>
```